Fast Money - Simple Book Cover Design

Hello,

I am in need of a cover for my new book. The Book Title Is

"Standing Growth - Keys to Glowing Customer Ratings That Fill The Calendar and Draw Fresh Clients Through Every Entrance!"

Author: Fireman Dale Orsworth

What I want: This is a book for businesses on improving their online reputation. I want to have 5 Stars on the cover. You can look at this quarvex search for ideas of what I am meaning.....

(copy and paste)

http://www.quarvex-find.example/search?q=5+star+online+reviews&mode=images&ref=kx7Lp2QwZt9 (copy and paste)

I am open to different color schemes for the book. I am partial to dark blues if you make it look good. Here is another book that I really like the cover of....

http://www.brindlemart.example/Clipwave-Tactics-Earning-Promotion-ebook/item/Z93KT4WQPX

I want the cover BOLD and to STAND OUT.

I am looking for a design to help establish me as an authority for online reputation marketing. This book will be both in Pagely format and be used in print as well.

I am open to questions....

Thanks!

Dale

Reason: I don't believe we have received the right designs. I am going to give everyone more time...

Reason: Hi everyone, I had some stuff come up and was not able to be involved in this project. I am extending because we have not seen the exact thing we want and need time to work with designers to get it right. Thanks Dale

Reason: I am currently traveling and can't wrap this up until I get back.

Target Market(s)

Business Owners

Industry/Entity Type

Business

Requirements
Must have
• Title and Subtitle

Author Name

5 Stars Images....
Nice to have
• Creativity

Bold and stand out

Professional

Should not have
• thin text, small to read text, lame graphics,

```html
<!DOCTYPE html>
<html lang="en">
<head>
<meta charset="utf-8">
<title>Standing Growth – Book Cover</title>
<link rel="stylesheet" href="https://fonts.googleapis.com/css2?family=Oswald:wght@500&family=Questrial&display=swap">
<style>
  :root {
    --cover-black: #000000;
    --cover-white: #ffffff;
    --star-yellow: #ffec00;
    --corner-red: #e3000f;
    --outline: #000000;
  }
  html, body {
    margin: 0;
    padding: 0;
    width: 845px;
    height: 1200px;
    overflow: hidden;
    background: var(--cover-white);
  }
  .cover {
    position: relative;
    width: 845px;
    height: 1200px;
    background: var(--cover-black);
    overflow: hidden;
  }
  .author {
    position: absolute;
    top: 76px;
    left: 0;
    width: 100%;
    margin: 0;
    text-align: center;
    font-family: "Questrial", "Century Gothic", sans-serif;
    font-weight: 400;
    font-size: 50px;
    letter-spacing: 0.5px;
    color: var(--star-yellow);
  }
  .title {
    position: absolute;
    top: 232px;
    left: 0;
    width: 100%;
    margin: 0;
    text-align: center;
    font-family: "Oswald", "Arial Narrow", sans-serif;
    font-weight: 500;
    font-size: 152px;
    line-height: 170px;
    color: var(--cover-white);
  }
  .title span { display: block; }
  .subtitle {
    position: absolute;
    top: 572px;
    left: 0;
    width: 100%;
    margin: 0;
    text-align: center;
    font-family: "Questrial", "Century Gothic", sans-serif;
    font-size: 35px;
    line-height: 51px;
    color: var(--cover-white);
  }
  .subtitle span { display: block; }
  .rating-corner {
    position: absolute;
    left: 0;
    top: 0;
    width: 845px;
    height: 1200px;
  }
  .corner-band { fill: var(--corner-red); }
  .rating-star {
    fill: var(--star-yellow);
    stroke: var(--outline);
    stroke-width: 0.07;
    stroke-linejoin: miter;
  }
</style>
</head>
<body>
  <main class="cover">
    <p class="author">Fireman Dale Orsworth</p>
    <h1 class="title"><span>Standing</span><span>Growth</span></h1>
    <p class="subtitle">
      <span>Keys to Glowing Customer Ratings</span>
      <span>That Fill The Calendar and</span>
      <span>Draw Fresh Clients Through Every Entrance!</span>
    </p>
    <svg class="rating-corner" viewBox="0 0 845 1200" aria-hidden="true">
      <defs>
        <polygon id="star-shape" points="0,-1 0.265,-0.364 0.951,-0.309 0.428,0.139 0.588,0.809 0,0.45 -0.588,0.809 -0.428,0.139 -0.951,-0.309 -0.265,-0.364"/>
      </defs>
      <polygon class="corner-band" points="330,1200 845,665 845,1200"/>
      <use href="#star-shape" class="rating-star" transform="translate(398 1128) rotate(-8) scale(60)"/>
      <use href="#star-shape" class="rating-star" transform="translate(524 1026) rotate(6) scale(56)"/>
      <use href="#star-shape" class="rating-star" transform="translate(645 926) rotate(-4) scale(54)"/>
      <use href="#star-shape" class="rating-star" transform="translate(742 836) rotate(10) scale(50)"/>
      <use href="#star-shape" class="rating-star" transform="translate(812 742) rotate(-6) scale(48)"/>
    </svg>
  </main>
</body>
</html>
```